Business Card Design

We are looking for a business card designed for our landscaping company. We do landscaping installation & Maintenance Services. We would like to see designs that have basic landscaping in background. We also think it is important to have both of our names and phone numbers on the card. We need something that stands out a little whether it is shape of the card or thickness or design.

Industry/Entity Type

Business

Contact Information for Business Card

Pale Ridge Yardworks, paleridgeyardworks@mailbrook.net, Dale Purvine 555-213-7690, Martin Kolbey 555-864-1037

```html
<!DOCTYPE html>
<html lang="en">
<head>
<meta charset="utf-8">
<title>Pale Ridge Yardworks – Business Card</title>
<link rel="stylesheet" href="https://fonts.googleapis.com/css2?family=Questrial&display=swap">
<style>
  :root {
    --page-bg: #eeeeec;
    --card-green: #2f5622;
    --card-green-deep: #27491c;
    --lime: #8cc63f;
    --lime-text: #9ccd4b;
    --white: #ffffff;
    --email-ink: #2a4d1d;
  }
  html, body {
    margin: 0;
    padding: 0;
    width: 848px;
    height: 1200px;
    overflow: hidden;
    background: var(--page-bg);
  }
  .business-card {
    position: absolute;
    left: 44px;
    top: 386px;
    width: 760px;
    height: 428px;
    overflow: hidden;
    background: radial-gradient(ellipse at 40% 45%, var(--card-green) 0%, var(--card-green-deep) 100%);
    box-shadow: 0 2px 10px rgba(0,0,0,0.12);
    font-family: "Questrial", "Century Gothic", sans-serif;
  }
  .card-accents {
    position: absolute;
    inset: 0;
  }
  .accent { fill: var(--lime); }
  .company-name {
    position: absolute;
    left: 84px;
    top: 90px;
    margin: 0;
    font-weight: 400;
    font-size: 22px;
    line-height: 40px;
    letter-spacing: 0.32em;
    text-transform: uppercase;
  }
  .company-name .line-top { display: block; color: var(--white); }
  .company-name .line-bottom { display: block; color: var(--lime-text); }
  .contacts {
    position: absolute;
    left: 84px;
    top: 220px;
    width: 620px;
    margin: 0;
    display: grid;
    grid-template-columns: 356px auto;
    row-gap: 18px;
    font-size: 23px;
    letter-spacing: 0.08em;
  }
  .contact-name { color: var(--lime-text); }
  .contact-phone { color: var(--white); letter-spacing: 0.14em; }
  .email {
    position: absolute;
    left: 84px;
    top: 370px;
    margin: 0;
    font-size: 23px;
    letter-spacing: 0.1em;
    color: var(--email-ink);
  }
</style>
</head>
<body>
  <section class="business-card" aria-label="Pale Ridge Yardworks business card">
    <svg class="card-accents" width="760" height="428" viewBox="0 0 760 428" aria-hidden="true">
      <path class="accent accent-top" d="M371,0 C430,0 440,45 505,45 L760,45 L760,0 Z"/>
      <path class="accent accent-bottom" d="M0,353 L560,353 C640,353 680,298 760,294 L760,428 L0,428 Z"/>
    </svg>
    <h1 class="company-name">
      <span class="line-top">Pale Ridge</span>
      <span class="line-bottom">Yardworks</span>
    </h1>
    <div class="contacts">
      <span class="contact-name">Dale Purvine</span>
      <span class="contact-phone">555-213-7690</span>
      <span class="contact-name">Martin Kolbey</span>
      <span class="contact-phone">555-864-1037</span>
    </div>
    <p class="email">paleridgeyardworks@mailbrook.net</p>
  </section>
</body>
</html>
```